Corvane wall and floor tiling

I would like you to design me a wrap for my work van, I will provide the logo I would like you to work off.
I’m happy for some slight little changes.
just need some creativity with the wrap design & background.
We are a tiling business in the construction industry.
Any designs are welcome but I do like what I have going on here and this type of font.
Show me what you got.
I would like the van to have a half wrap not just the side stickers like it shows in the photos.
The new mobile numbers I would like on the wrap are
0491638425
0412864359
We cover Tiling, screeding , waterproofing

Industry/Entity Type

Construction

Colors

Designer to choose colors to be used in the design.

Requirements
Must have
• Brindlo & snapveil logo somewhere small. Tiling, Waterproofing & Screeding

```html
<!DOCTYPE html>
<html lang="en">
<head>
<meta charset="utf-8">
<title>Corvane Wall &amp; Floor Tiling – Van Wrap</title>
<link rel="stylesheet" href="https://fonts.googleapis.com/css2?family=Exo+2:wght@800&family=Montserrat:wght@600;700&display=swap">
<style>
  :root {
    --brand-blue: #1e8fe0;
    --wrap-blue: #2a9be6;
    --band-dark: #3a3b3d;
    --phone-grey: #8a8c8f;
    --body-white: #f7f8f9;
    --outline: #c9ccd0;
    --tyre: #222326;
    --hub: #b9bcc0;
    --glass: #6f7276;
    --page: #ffffff;
  }
  html, body {
    margin: 0;
    width: 1200px;
    height: 1200px;
    overflow: hidden;
    background: var(--page);
  }
  .wrap-sheet { display: block; width: 1200px; height: 1200px; }
  .van-body { fill: var(--body-white); stroke: var(--outline); stroke-width: 1.5; }
  .wrap-blue { fill: var(--wrap-blue); }
  .wrap-band { fill: var(--band-dark); }
  .bumper { fill: var(--tyre); }
  .glass { fill: var(--glass); }
  .panel-line { fill: none; stroke: var(--outline); stroke-width: 1.2; }
  .tyre { fill: var(--tyre); }
  .hub { fill: var(--hub); stroke: #8f9397; stroke-width: 2; }
  .headlight { fill: #d9dcdf; stroke: #9ea2a6; }
  .ground-shadow { fill: #000; opacity: .18; }
  .brand-mark { fill: var(--brand-blue); }
  .brand-name {
    font-family: "Exo 2", sans-serif; font-weight: 800;
    fill: var(--brand-blue); font-size: 64px; letter-spacing: 2px;
  }
  .brand-tagline {
    font-family: "Exo 2", sans-serif; font-weight: 800;
    fill: var(--brand-blue); font-size: 25px; letter-spacing: .5px;
  }
  .service-list {
    font-family: "Montserrat", sans-serif; font-weight: 600;
    fill: #fff; font-size: 13.5px; letter-spacing: .6px;
  }
  .service-dot { fill: var(--wrap-blue); }
  .phone { font-family: "Montserrat", sans-serif; font-weight: 700; font-size: 19px; letter-spacing: 1.5px; }
  .phone-primary { fill: var(--brand-blue); }
  .phone-secondary { fill: var(--phone-grey); }
  .phone-on-band { fill: #fff; }
</style>
</head>
<body>
<svg class="wrap-sheet" viewBox="0 0 960 960" xmlns="http://www.w3.org/2000/svg">
  <defs>
    <path id="van-outline" d="M70,95 Q72,78 95,76 L630,74 Q655,74 668,84 L840,190 Q862,205 880,225 L905,250 Q915,262 915,280 L915,370 Q915,385 900,385 L795,385 A60,60 0 0 0 675,385 L305,385 A62,62 0 0 0 180,385 L75,385 Q60,385 60,370 L60,110 Q60,97 70,95 Z"/>
    <clipPath id="van-clip"><use href="#van-outline"/></clipPath>
    <g id="van-chassis">
      <path class="glass" d="M650,92 L818,94 Q834,102 845,132 L852,186 L664,190 Q650,188 650,175 Z"/>
      <path class="panel-line" d="M640,86 L640,380 M100,92 L100,120 M648,205 L648,212"/>
      <rect x="655" y="204" width="26" height="6" rx="3" fill="#4a4c50"/>
      <rect class="headlight" x="878" y="240" width="32" height="30" rx="5"/>
      <rect class="bumper" x="60" y="335" width="60" height="50" rx="6"/>
      <rect class="bumper" x="862" y="320" width="54" height="65" rx="8"/>
      <ellipse class="ground-shadow" cx="485" cy="432" rx="430" ry="7"/>
      <circle class="tyre" cx="242" cy="382" r="50"/>
      <circle class="hub" cx="242" cy="382" r="32"/>
      <circle class="tyre" cx="735" cy="382" r="50"/>
      <circle class="hub" cx="735" cy="382" r="32"/>
    </g>
    <g id="brand-lockup">
      <rect class="brand-mark" x="105" y="118" width="80" height="80" rx="4"/>
      <text class="brand-name" x="250" y="172">CORVANE</text>
      <text class="brand-tagline" x="285" y="212">WALL &amp; FLOOR TILING</text>
    </g>
  </defs>

  <!-- Option A: diagonal sweep -->
  <g class="van van-diagonal">
    <use class="van-body" href="#van-outline"/>
    <g clip-path="url(#van-clip)">
      <path class="wrap-blue" d="M50,240 L662,318 Q672,355 668,400 L50,400 Z"/>
      <path class="wrap-band" d="M50,212 L664,292 L662,320 L50,241 Z"/>
    </g>
    <use href="#van-chassis"/>
    <use href="#brand-lockup"/>
    <g transform="rotate(7.4 88 232)">
      <text class="service-list" x="88" y="236">TILING <tspan class="service-dot">●</tspan> SCREEDING <tspan class="service-dot">●</tspan> WATERPROOFING <tspan class="service-dot">●</tspan> BATHROOM RENO’S</text>
    </g>
    <text class="phone phone-primary" x="684" y="256">049.163.8425</text>
    <text class="phone phone-secondary" x="684" y="280">041.286.4359</text>
  </g>

  <!-- Option B: straight band -->
  <g class="van van-straight" transform="translate(0 470)">
    <use class="van-body" href="#van-outline"/>
    <g clip-path="url(#van-clip)">
      <rect class="wrap-band" x="50" y="232" width="830" height="28"/>
      <rect class="wrap-blue" x="50" y="264" width="880" height="140"/>
    </g>
    <use href="#van-chassis"/>
    <use href="#brand-lockup"/>
    <text class="service-list" x="102" y="251">TILING <tspan class="service-dot">●</tspan> SCREEDING <tspan class="service-dot">●</tspan> WATERPROOFING <tspan class="service-dot">●</tspan> BATHROOM RENO’S</text>
    <text class="phone phone-primary" x="682" y="226">049.163.8425</text>
    <text class="phone phone-on-band" x="682" y="254">041.286.4359</text>
  </g>
</svg>
</body>
</html>
```